Brackwell Renovations needs a website.

I need a platform for clients to go and learn about what my company does, see pictures of projects, and contact me about their projects. I am a residential remodeler specializing in general contracting services for kitchens, bathrooms, basements, additions, custom interiors, and more. I have attached my logo to be incorporated.

```html
<!DOCTYPE html>
<html lang="en">
<head>
<meta charset="utf-8">
<title>Brackwell Renovations</title>
<link href="https://fonts.googleapis.com/css2?family=Poppins:wght@400;500;600;700&display=swap" rel="stylesheet">
<style>
:root{
  --green:#6fa76a;
  --green-dark:#5a9456;
  --ink:#1c1c1c;
  --muted:#7a7a7a;
  --light:#f4f4f4;
  --panel:#e6e6e6;
  --white:#ffffff;
  --black:#000000;
}
*{box-sizing:border-box;margin:0;padding:0}
html,body{width:1200px;height:4790px;overflow:hidden}
body{position:relative;font-family:'Poppins',sans-serif;color:var(--ink);background:var(--white)}
.abs{position:absolute}
.btn{position:absolute;display:flex;align-items:center;justify-content:center;border-radius:30px;font-weight:600;font-size:14px;text-transform:uppercase;letter-spacing:.3px}
.btn-green{background:var(--green);color:var(--white)}
.btn-outline{border:2px solid var(--green);color:var(--green);background:var(--white)}
.btn-ghost{border:2px solid var(--white);color:var(--white)}
.rule{position:absolute;height:3px;width:74px;background:var(--green);left:50%;margin-left:-37px}
.section-title{position:absolute;left:0;width:1200px;text-align:center;font-weight:600;font-size:30px;text-transform:uppercase}
.brand{position:absolute;display:flex;align-items:center;gap:12px;font-weight:600;font-size:22px;line-height:1;text-transform:uppercase;color:var(--ink)}
.brand-mark{width:62px;height:62px;border-radius:50%;border:3px solid var(--green)}

/* header */
.topbar{left:433px;top:0;width:767px;height:38px;background:var(--green);border-bottom-left-radius:30px;color:var(--white);font-size:15px}
.topbar .social{position:absolute;left:50px;top:11px;display:flex;gap:12px}
.topbar .social span{width:16px;height:16px;border-radius:50%;background:var(--white)}
.topbar .contact{position:absolute;right:50px;top:8px;display:flex;gap:28px;align-items:center}
.topbar .contact span{display:flex;align-items:center;gap:8px}
.nav{left:435px;top:76px;display:flex;gap:46px;font-size:14px;font-weight:500;text-transform:uppercase}

/* hero */
.hero{left:0;top:130px;width:1200px;height:740px;overflow:hidden}
.hero-photo{position:absolute;inset:0;background:linear-gradient(180deg,#3a3834 0%,#2b2925 45%,#4a4038 75%,#5b5149 100%)}
.hero-shade{position:absolute;inset:0;background:rgba(0,0,0,.35)}
.hero-welcome{top:200px;width:1200px;text-align:center;color:var(--green);font-size:20px;font-weight:500}
.hero-title{top:232px;width:1200px;text-align:center;color:var(--white);font-size:52px;font-weight:600;text-transform:uppercase}
.hero-text{top:302px;left:270px;width:660px;text-align:center;color:var(--white);font-size:16px;line-height:1.3}

/* about */
.about-img{border-radius:20px;border:5px solid var(--white);box-shadow:0 4px 18px rgba(0,0,0,.15)}
.about-title{left:575px;top:1022px;font-size:30px;font-weight:600}
.about-copy{left:580px;width:525px;font-size:14px;line-height:1.55;color:var(--muted)}
.feature{top:1425px;display:flex;gap:22px;align-items:center}
.feature h4{font-size:12px;font-weight:500;text-transform:uppercase;margin-bottom:6px}
.feature p{font-size:11px;color:var(--muted);width:190px;line-height:1.4}

/* what we do */
.wwd-band{left:0;top:1605px;width:1200px;height:412px;background:var(--green)}
.wwd-title{top:1682px;color:var(--white)}
.wwd-text{left:330px;top:1740px;width:540px;text-align:center;font-size:14px;line-height:1.55;color:var(--white)}
.svc-card{top:1845px;width:273px;height:380px;background:var(--white);border-radius:16px;box-shadow:0 6px 24px rgba(0,0,0,.12);text-align:center}
.svc-photo{position:absolute;left:10px;top:10px;width:253px;height:160px;border-radius:10px 10px 0 0;background:linear-gradient(180deg,#4a4744,#8b7d6c)}
.svc-icon{position:absolute;left:98px;top:135px;width:76px;height:76px;border-radius:50%;background:#cfcfcf;border:4px solid var(--white)}
.svc-card h3{position:absolute;top:228px;width:100%;font-size:13px;font-weight:600;text-transform:uppercase}
.svc-card p{position:absolute;left:35px;top:255px;width:203px;font-size:11px;line-height:1.3;color:var(--muted)}
.svc-card .btn{left:70px;top:325px;width:132px;height:34px;font-size:11px}
.arrow{position:absolute;width:24px;height:30px}

/* projects */
.proj{background:linear-gradient(160deg,#8b8070,#c9b79a)}
.proj-title{left:420px;top:2870px;color:var(--white);font-size:26px;font-weight:500;text-transform:uppercase}
.proj-text{left:420px;top:2925px;width:320px;color:var(--white);font-size:11px;line-height:1.3}

/* reviews */
.review{top:3275px;width:293px;height:230px;background:var(--white);border-radius:28px;box-shadow:0 6px 26px rgba(0,0,0,.1);padding:40px 30px 0}
.review .stars{color:var(--green);font-size:16px;letter-spacing:4px;margin-left:5px}
.review p{font-size:10.5px;line-height:1.3;color:var(--muted);text-align:center;margin-top:8px}
.review .who{position:absolute;left:38px;top:174px;display:flex;align-items:center;gap:12px}
.review .avatar{width:40px;height:40px;border-radius:50%;background:#d7c7b0}
.review .who b{display:block;font-size:10px;font-weight:600}
.review .who small{font-size:10px;color:var(--green)}
.dot{position:absolute;top:3565px;width:20px;height:20px;border-radius:50%;background:var(--green)}
.dot.open{background:var(--white);border:2px solid var(--green)}

/* quote */
.quote-box{left:128px;top:3690px;width:942px;height:495px;background:var(--panel);border-radius:16px}
.field{position:absolute;height:52px;background:var(--white);border:1px solid #d8d8d8;font-size:13px;color:#9a9a9a;padding:17px 30px;text-transform:uppercase}

/* footer */
.footer{left:0;top:4250px;width:1200px;height:540px}
.foot-head{color:var(--white);font-size:26px;font-weight:500;text-transform:uppercase}
.foot-list{list-style:none;color:var(--white);font-size:18px}
.foot-list li{display:flex;align-items:center;gap:14px;margin-bottom:15px}
.foot-list .bullet{width:18px;height:18px;border-radius:50%;border:2px solid var(--white)}
.foot-contact{color:var(--white);font-size:18px}
.foot-contact div{display:flex;gap:16px;align-items:flex-start;margin-bottom:20px;line-height:1.2}
.foot-contact .ic{width:24px;height:24px;border-radius:50%;background:var(--white);flex:none}
.foot-social{left:127px;top:4627px;display:flex;gap:14px}
.foot-social span{width:40px;height:40px;border-radius:50%;border:3px solid var(--white);background:var(--green)}
.copyright{left:0;top:4750px;width:1200px;text-align:center;color:var(--white);font-size:14px}
</style>
</head>
<body>

<!-- header -->
<div class="brand" style="left:48px;top:34px;font-size:21px">
  <span class="brand-mark"></span><span>Brackwell<br>Renovations</span>
</div>
<div class="abs topbar">
  <div class="social"><span></span><span></span><span></span></div>
  <div class="contact">
    <span><svg width="20" height="20" viewBox="0 0 20 20"><circle cx="10" cy="10" r="10" fill="#fff"/><path d="M6 6l3 0 1 3-2 1a6 6 0 0 0 3 3l1-2 3 1v3c-5 0-9-4-9-9z" fill="#6fa76a"/></svg>(555) 014 2290</span>
    <span><svg width="20" height="20" viewBox="0 0 20 20"><circle cx="10" cy="10" r="10" fill="#fff"/><path d="M6 6l3 0 1 3-2 1a6 6 0 0 0 3 3l1-2 3 1v3c-5 0-9-4-9-9z" fill="#6fa76a"/></svg>(555) 014 2290</span>
  </div>
</div>
<nav class="abs nav"><span>Home</span><span>About</span><span>Services</span><span>Projects</span><span>Contact</span></nav>
<div class="btn btn-green" style="left:996px;top:62px;width:168px;height:46px">Get a Quote</div>

<!-- hero -->
<section class="abs hero">
  <div class="hero-photo" role="img" aria-label="Modern dark kitchen with wooden dining table and black chairs"></div>
  <div class="hero-shade"></div>
  <div class="abs hero-welcome">Welcome to</div>
  <h1 class="abs hero-title">Brackwell Renovations</h1>
  <p class="abs hero-text">Lorem ipsum dolor sit amet, consectetur adipiscing elit, sed do eiusmod tempor incididunt ut labore et dolore magna aliqua.</p>
  <div class="btn btn-green" style="left:425px;top:368px;width:166px;height:44px">Get a Quote</div>
  <div class="btn btn-ghost" style="left:616px;top:368px;width:168px;height:44px">Read More</div>
  <svg class="abs" style="left:0;top:600px" width="1200" height="140" viewBox="0 0 1200 140" preserveAspectRatio="none">
    <path d="M0 110 C200 40 420 60 640 90 C850 120 1020 110 1200 60 L1200 140 L0 140Z" fill="#6fa76a"/>
    <path d="M0 132 C220 60 430 80 640 105 C860 130 1030 125 1200 85 L1200 140 L0 140Z" fill="#fff"/>
  </svg>
</section>

<!-- about -->
<div class="abs about-img" style="left:108px;top:952px;width:246px;height:322px;background:linear-gradient(180deg,#e9e1cf,#a3784b)" role="img" aria-label="Bright hallway interior with wood panels"></div>
<div class="abs about-img" style="left:252px;top:1080px;width:248px;height:248px;background:linear-gradient(160deg,#d8d2c6,#5a3c28)" role="img" aria-label="Modern bathroom vanity with dark wood cabinet"></div>
<h2 class="abs about-title">About Us</h2>
<div class="abs" style="left:575px;top:1065px;width:74px;height:3px;background:var(--green)"></div>
<p class="abs about-copy" style="top:1084px">We specialize in turning outdated kitchens and bathrooms into beautiful, functional spaces you'll love. Whether you're dreaming of a sleek modern kitchen, a cozy farmhouse bath, or a luxurious spa-like retreat, our team delivers exceptional craftsmanship and personalized service.</p>
<p class="abs about-copy" style="top:1178px">We specialize in turning outdated kitchens and bathrooms into beautiful, functional spaces you'll love. Whether you're dreaming of a sleek modern kitchen, a cozy farmhouse bath, or a luxurious spa-like retreat, our team delivers exceptional craftsmanship and personalized service.</p>
<div class="btn btn-green" style="left:580px;top:1283px;width:168px;height:44px">Read More</div>

<div class="abs feature" style="left:100px">
  <svg width="92" height="92" viewBox="0 0 92 92" fill="none" stroke="#6fa76a" stroke-width="2.5"><rect x="4" y="44" width="84" height="42"/><rect x="10" y="52" width="26" height="28"/><line x1="46" y1="44" x2="46" y2="86"/><rect x="4" y="10" width="38" height="10"/><rect x="50" y="4" width="38" height="26"/></svg>
  <div><h4>Custom Designs</h4><p>We specialize in turning outdated kitchens and bathrooms</p></div>
</div>
<div class="abs feature" style="left:450px">
  <svg width="100" height="92" viewBox="0 0 100 92" fill="none" stroke="#6fa76a" stroke-width="2.5"><circle cx="50" cy="22" r="12"/><circle cx="22" cy="40" r="10"/><circle cx="78" cy="40" r="10"/><path d="M30 88v-20a20 20 0 0 1 40 0v20"/><path d="M4 88v-14a18 18 0 0 1 22-16"/><path d="M96 88v-14a18 18 0 0 0-22-16"/></svg>
  <div><h4>Experienced Professionals</h4><p>We specialize in turning outdated kitchens and bathrooms</p></div>
</div>
<div class="abs feature" style="left:812px">
  <svg width="96" height="92" viewBox="0 0 96 92" fill="none" stroke="#6fa76a" stroke-width="2.5"><circle cx="46" cy="46" r="40" stroke-dasharray="14 8"/><rect x="30" y="22" width="40" height="48"/><circle cx="34" cy="56" r="12"/><path d="M28 56l5 5 8-9"/><line x1="44" y1="32" x2="62" y2="32"/><line x1="44" y1="42" x2="62" y2="42"/></svg>
  <div><h4>Stress Free Process</h4><p>We specialize in turning outdated kitchens and bathrooms</p></div>
</div>

<!-- what we do -->
<div class="abs wwd-band"></div>
<h2 class="section-title wwd-title">What We Do</h2>
<div class="abs" style="left:563px;top:1727px;width:74px;height:3px;background:var(--white)"></div>
<p class="abs wwd-text">We specialize in turning outdated kitchens and bathrooms into beautiful, functional spaces you'll love. Whether you're dreaming of a sleek modern kitchen.</p>

<div class="abs svc-card" style="left:143px">
  <div class="svc-photo" role="img" aria-label="Modern kitchen with dark cabinets"></div><div class="svc-icon"></div>
  <h3>Kitchen Remodeling</h3><p>Lorem ipsum dolor sit amet, consectetur adipiscing elit, sed do eiusmod tempor incididunt ut labore et dolore magna aliqua.</p>
  <div class="btn btn-outline">Read More</div>
</div>
<div class="abs svc-card" style="left:463px">
  <div class="svc-photo" role="img" aria-label="Modern kitchen with dark cabinets"></div><div class="svc-icon"></div>
  <h3>Bathroom Remodeling</h3><p>Lorem ipsum dolor sit amet, consectetur adipiscing elit, sed do eiusmod tempor incididunt ut labore et dolore magna aliqua.</p>
  <div class="btn btn-outline">Read More</div>
</div>
<div class="abs svc-card" style="left:783px">
  <div class="svc-photo" role="img" aria-label="Modern kitchen with dark cabinets"></div><div class="svc-icon"></div>
  <h3>Custom Design</h3><p>Lorem ipsum dolor sit amet, consectetur adipiscing elit, sed do eiusmod tempor incididunt ut labore et dolore magna aliqua.</p>
  <div class="btn btn-outline">Read More</div>
</div>
<svg class="arrow" style="left:42px;top:2042px" viewBox="0 0 24 30"><path d="M18 3L6 15l12 12" fill="none" stroke="#6fa76a" stroke-width="3"/></svg>
<svg class="arrow" style="left:1134px;top:2042px" viewBox="0 0 24 30"><path d="M6 3l12 12L6 27" fill="none" stroke="#6fa76a" stroke-width="3"/></svg>

<!-- projects -->
<h2 class="section-title" style="top:2342px">Recent Projects</h2>
<div class="rule" style="top:2388px"></div>
<div class="abs proj" style="left:0;top:2460px;width:365px;height:283px;background:linear-gradient(160deg,#6b5a48,#e6dccb)" role="img" aria-label="Hallway with wood panel walls"></div>
<div class="abs proj" style="left:0;top:2762px;width:365px;height:283px;background:linear-gradient(160deg,#b7ab95,#6f6150)" role="img" aria-label="Living room with armchair and large window"></div>
<div class="abs proj" style="left:385px;top:2460px;width:423px;height:585px;background:linear-gradient(180deg,#3f4246,#6d6f70 60%,#8a8277)" role="img" aria-label="Walk-in shower with grey tiles"></div>
<div class="abs proj-title">Poject Title</div>
<p class="abs proj-text">Lorem ipsum dolor sit amet, consectetur adipiscing elit, sed do eiusmod tempor incididunt ut labore et dolore magna aliqua.</p>
<div class="abs proj" style="left:833px;top:2460px;width:367px;height:283px;background:linear-gradient(160deg,#e9e1d3,#b8825e)" role="img" aria-label="Kitchen counter with plants and wood cabinets"></div>
<div class="abs proj" style="left:833px;top:2762px;width:367px;height:283px;background:linear-gradient(180deg,#4b4946,#a98a68)" role="img" aria-label="Modern kitchen with open shelving"></div>

<!-- reviews -->
<h2 class="section-title" style="top:3170px">What Customer Says</h2>
<div class="rule" style="top:3216px"></div>
<div class="abs review" style="left:128px"><div class="stars">★★★★★</div><p>The sales dashboards are fantastic! They provide clear, real-time insights into our performance, which has sparked healthy competition within our office. Everyone is motivated to reach their targets, and our sales numbers have never been better!</p><div class="who"><span class="avatar" role="img" aria-label="Client portrait"></span><div><b>JORDAN P.</b><small>Owner</small></div></div></div>
<div class="abs review" style="left:453px"><div class="stars">★★★★★</div><p>The sales dashboards are fantastic! They provide clear, real-time insights into our performance, which has sparked healthy competition within our office. Everyone is motivated to reach their targets, and our sales numbers have never been better!</p><div class="who"><span class="avatar" role="img" aria-label="Client portrait"></span><div><b>JORDAN P.</b><small>Owner</small></div></div></div>
<div class="abs review" style="left:777px"><div class="stars">★★★★★</div><p>The sales dashboards are fantastic! They provide clear, real-time insights into our performance, which has sparked healthy competition within our office. Everyone is motivated to reach their targets, and our sales numbers have never been better!</p><div class="who"><span class="avatar" role="img" aria-label="Client portrait"></span><div><b>JORDAN P.</b><small>Owner</small></div></div></div>
<svg class="arrow" style="left:38px;top:3375px" viewBox="0 0 24 30"><path d="M18 3L6 15l12 12" fill="none" stroke="#6fa76a" stroke-width="3"/></svg>
<svg class="arrow" style="left:1130px;top:3375px" viewBox="0 0 24 30"><path d="M6 3l12 12L6 27" fill="none" stroke="#6fa76a" stroke-width="3"/></svg>
<span class="dot" style="left:555px"></span><span class="dot open" style="left:585px"></span><span class="dot" style="left:615px"></span>

<!-- quote -->
<div class="abs quote-box"></div>
<h2 class="section-title" style="top:3735px">Get a Quote</h2>
<div class="rule" style="top:3780px"></div>
<div class="field" style="left:183px;top:3825px;width:403px">Full Name</div>
<div class="field" style="left:607px;top:3825px;width:403px">Email Address</div>
<div class="field" style="left:183px;top:3895px;width:403px">Phone Number</div>
<div class="field" style="left:607px;top:3895px;width:403px">Select Service</div>
<div class="field" style="left:183px;top:3970px;width:827px;height:98px">Additional Message</div>
<div class="btn btn-green" style="left:496px;top:4105px;width:202px;height:44px">Submit Details</div>

<!-- footer -->
<div class="abs footer">
  <svg class="abs" style="left:0;top:0" width="1200" height="540" viewBox="0 0 1200 540" preserveAspectRatio="none">
    <path d="M0 50 C240 -10 480 40 720 50 C930 60 1080 40 1200 0 L1200 540 L0 540Z" fill="#6fa76a"/>
    <path d="M0 80 C240 20 480 70 720 80 C930 88 1080 70 1200 30 L1200 540 L0 540Z" fill="#000"/>
  </svg>
</div>
<div class="abs" style="left:117px;top:4500px;width:253px;height:88px;background:var(--white)"></div>
<div class="brand" style="left:135px;top:4518px;font-size:19px"><span class="brand-mark" style="width:50px;height:50px"></span><span>Brackwell<br>Renovations</span></div>
<div class="abs foot-social"><span></span><span></span><span></span><span></span></div>

<div class="abs foot-head" style="left:465px;top:4455px">Quick Links</div>
<ul class="abs foot-list" style="left:468px;top:4520px">
  <li><span class="bullet"></span>Home</li><li><span class="bullet"></span>About</li><li><span class="bullet"></span>Pricing</li><li><span class="bullet"></span>Contact</li>
</ul>
<div class="abs foot-head" style="left:800px;top:4455px">Contact</div>
<div class="abs foot-contact" style="left:805px;top:4532px">
  <div><span class="ic"></span>+1 555-014-2290</div>
  <div><span class="ic"></span>hello@brackwell-build.com</div>
  <div><span class="ic"></span>118 Harrow Lane<br>Stonebridge, SC 29000, USA</div>
</div>
<div class="abs" style="left:125px;top:4726px;width:975px;height:1px;background:#444"></div>
<div class="abs copyright">Copyright© 2025 Brackwell renovations,. All rights reserved.</div>

</body>
</html>
```